Business card design needed

Business Card design required for new small plumbing business.
Would like a logo/text look that is simple and unique and does not have to be representative of a plumbing company (ie. having a cartoon plumber or toilet etc) as the companyname is self explanatory.
Would like the main colour to be green (lime green).
Updates

Industry/Entity Type

Plumber

Contact Information for Business Card

BRAVELL PLUMBING
ABN 61 904 127 558 003

Trevor Hasketh
Licensed Plumber 83615
Phone: 0412 870 245

27 Bravell Drive,
Harrowdale. 3877 Eastmere

Email: bravellplumbing@mailnest.example

Logo Text

Bravell Plumbing

Logo styles of interest
Character Logo
Wordmark Logo
Lettermark Logo

```html
<!DOCTYPE html>
<html lang="en">
<head>
<meta charset="utf-8">
<title>Bravell Plumbing – Business Card</title>
<link rel="stylesheet" href="https://fonts.googleapis.com/css2?family=Fira+Sans:wght@400;500;600&display=swap">
<style>
  :root {
    --lime: #b8cf12;
    --ink: #545454;
    --paper: #ffffff;
  }
  html, body {
    margin: 0;
    padding: 0;
    overflow: hidden;
    background: var(--paper);
  }
  .card {
    position: relative;
    width: 1200px;
    height: 693px;
    background: var(--paper);
    font-family: "Fira Sans", sans-serif;
    color: var(--ink);
    overflow: hidden;
  }
  .card > * {
    position: absolute;
    left: 0;
    width: 100%;
    margin: 0;
    text-align: center;
    white-space: nowrap;
    line-height: 1;
  }
  .brand {
    top: 84px;
    font-size: 86px;
    font-weight: 500;
    color: var(--lime);
    letter-spacing: 0.2em;
    padding-left: 0.2em;
    box-sizing: border-box;
  }
  .holder-name {
    top: 214px;
    font-size: 48px;
    font-weight: 600;
  }
  .licence {
    top: 281px;
    font-size: 48px;
    font-weight: 600;
  }
  .contact {
    font-size: 45px;
    font-weight: 400;
  }
  .contact .label,
  .contact .bracket {
    color: var(--lime);
  }
  .contact-phone { top: 370px; }
  .contact-address { top: 427px; }
  .contact-email { top: 484px; }
  .abn {
    top: 578px;
    font-size: 37px;
    font-weight: 400;
  }
</style>
</head>
<body>
  <main class="card">
    <h1 class="brand">BRAVELL PLUMBING</h1>
    <p class="holder-name">Trevor Hasketh</p>
    <p class="licence">Licensed Plumber 83615</p>
    <p class="contact contact-phone"><span class="label">P</span> <span class="bracket">[</span> 0412 870 245 <span class="bracket">]</span></p>
    <p class="contact contact-address"><span class="label">A</span> <span class="bracket">[</span> 27 Bravell Drive, Harrowdale, 3877 Eastmere <span class="bracket">]</span></p>
    <p class="contact contact-email"><span class="label">E</span> <span class="bracket">[</span> bravellplumbing@mailnest.example <span class="bracket">]</span></p>
    <p class="abn">ABN 61 904 127 558 003</p>
  </main>
</body>
</html>
```